KT Crewing business card

Require business card which includes:
Company name: KT CREWING PTY LTD
Email: Mick@ktcrewing.com.au
Phone: 0431 556 208
ACN: 517 238 649

slogan: Onsite Auto Electrician Labour hire

Details and logo on top side
Logo only on bottom side

colour codes : #F15A29 , #939598

Target Market(s)

Western Australia mining sector

Industry/Entity Type

Mining

Contact Information for Business Card

Require business card which includes: Company name: KT CREWING PTY LTD Email: Mick@ktcrewing.com.au Phone: 0431 556 208 ACN: 517 238 649 slogan: Onsite Auto Electrician Labour hire Details and logo on top side Logo only on bottom side colour codes : #F15A29 , #939598

Colors
EE7325
F08F49
F5BC92
FAE3D3
FDF4ED

Requirements
Must have
• double sided

```html
<!DOCTYPE html>
<html lang="en">
<head>
<meta charset="utf-8">
<title>KT Crewing business card</title>
<link href="https://fonts.googleapis.com/css2?family=Exo+2:wght@400;700;800&display=swap" rel="stylesheet">
<style>
  :root {
    --brand-orange: #E05226;
    --brand-grey: #8C8D90;
    --card-white: #F1F1F1;
    --page-bg: #E9E4DC;
    --text-white: #FFFFFF;
  }
  * { box-sizing: border-box; margin: 0; padding: 0; }
  html, body { width: 1200px; height: 900px; overflow: hidden; }
  body {
    background: var(--page-bg);
    font-family: "Exo 2", sans-serif;
    position: relative;
  }
  .card {
    position: absolute;
    left: 290px;
    width: 620px;
    height: 354px;
    overflow: hidden;
    box-shadow: 0 6px 18px rgba(0,0,0,0.12);
  }
  .card--back { top: 70px; background: var(--brand-orange); }
  .card--front { top: 476px; background: var(--card-white); }

  /* back side */
  .back-brand {
    position: absolute;
    left: 44px;
    bottom: 40px;
    display: flex;
    align-items: center;
    gap: 12px;
    white-space: nowrap;
  }
  .brand-square {
    width: 16px;
    height: 16px;
    flex: none;
    background: var(--text-white);
  }
  .back-brand .brand-name {
    color: var(--text-white);
    font-weight: 800;
    font-size: 40px;
    line-height: 1;
  }
  .slogan {
    position: absolute;
    left: 318px;
    bottom: 72px;
    color: var(--text-white);
    font-weight: 700;
    font-size: 13px;
    letter-spacing: 0.5px;
    text-transform: uppercase;
    white-space: nowrap;
  }

  /* front side */
  .front-brand {
    position: absolute;
    left: 40px;
    top: 110px;
    display: flex;
    align-items: center;
    gap: 12px;
    white-space: nowrap;
  }
  .front-brand .brand-square { background: var(--brand-grey); }
  .front-brand .brand-name {
    color: var(--brand-orange);
    font-weight: 800;
    font-size: 44px;
    line-height: 1;
  }
  .divider {
    position: absolute;
    left: 40px;
    top: 205px;
    width: 320px;
    height: 1px;
    background: var(--brand-orange);
  }
  .details {
    position: absolute;
    left: 380px;
    top: 70px;
    width: 230px;
  }
  .person-name {
    color: var(--brand-grey);
    font-weight: 800;
    font-size: 22px;
    letter-spacing: 0.5px;
    text-transform: uppercase;
    white-space: nowrap;
  }
  .person-role {
    color: var(--brand-grey);
    font-size: 12px;
    margin: 2px 0 0 14px;
  }
  .contact-list { list-style: none; margin: 12px 0 0 14px; }
  .contact-item {
    display: flex;
    align-items: center;
    gap: 8px;
    color: var(--brand-grey);
    font-size: 15px;
    line-height: 1.45;
    white-space: nowrap;
  }
  .contact-item svg { width: 12px; height: 12px; flex: none; }
  .company-name {
    color: var(--brand-orange);
    font-weight: 800;
    font-size: 17px;
    margin: 14px 0 0 14px;
    white-space: nowrap;
  }
  .acn-band {
    position: absolute;
    left: 396px;
    right: 0;
    top: 222px;
    height: 30px;
    background: var(--brand-orange);
    color: var(--text-white);
    font-size: 13px;
    line-height: 30px;
    padding-left: 28px;
    white-space: nowrap;
  }
</style>
</head>
<body>

  <section class="card card--back" aria-label="Card back">
    <div class="back-brand">
      <span class="brand-square"></span>
      <span class="brand-name">KT Crewing</span>
    </div>
    <p class="slogan">Onsite Auto Electrician Labour Hire</p>
  </section>

  <section class="card card--front" aria-label="Card front">
    <div class="front-brand">
      <span class="brand-square"></span>
      <span class="brand-name">KT Crewing</span>
    </div>
    <div class="divider"></div>

    <div class="details">
      <h1 class="person-name">Corey Walsh</h1>
      <p class="person-role">Director/ CEO</p>
      <ul class="contact-list">
        <li class="contact-item">
          <svg viewBox="0 0 24 24" aria-hidden="true"><path fill="#E05226" d="M6.6 10.8a15.2 15.2 0 0 0 6.6 6.6l2.2-2.2a1 1 0 0 1 1-.25 11.4 11.4 0 0 0 3.6.57 1 1 0 0 1 1 1V20a1 1 0 0 1-1 1A17 17 0 0 1 3 4a1 1 0 0 1 1-1h3.5a1 1 0 0 1 1 1c0 1.25.2 2.45.57 3.57a1 1 0 0 1-.25 1z"/></svg>
          0431 556 208
        </li>
        <li class="contact-item">
          <svg viewBox="0 0 24 24" aria-hidden="true"><path fill="#E05226" d="M2 5h20v14H2z"/><path fill="none" stroke="#F1F1F1" stroke-width="1.8" d="M2 5l10 8 10-8"/></svg>
          Mick@ktcrewing.com.au
        </li>
      </ul>
      <p class="company-name">KT CREWING PTY LTD</p>
    </div>

    <div class="acn-band">ACN: 517 238 649</div>
  </section>

</body>
</html>
```